Kestrel Orchard Fliers and logo design

We need to design a product logo and some informational fliers for a pebble quest.
I have attached our Kestrel Orchard logo - colours need to be complimentary but not the same, we would like fresh, funky but still professional. We generally communicate in a fairly casual way to reach our market. (We don't like boring)
Clear and simple - not too busy
images are good but not actual photos
Here is our website to give you an idea www.kestrelorchard.co.nz
The flier is a 3 page document.
The logo is to say Pebble Quest. The challenge is based on exercise, connecting with people, giving, learning and taking notice (The 7 stones of Marlow) Once agin the logo needs to be complementary but not the same.
The Kestrel orchard logo needs to be on the fliers but the pebble quest logo is separate.
Thanks very much!!

```html
<!DOCTYPE html>
<html lang="en">
<head>
<meta charset="utf-8">
<title>Kestrel Orchard – Pebble Quest fliers</title>
<link href="https://fonts.googleapis.com/css2?family=Oswald:wght@500;600&family=Open+Sans:wght@400;600;700&display=swap" rel="stylesheet">
<style>
:root{
  --backdrop:#4b4b4b;
  --paper:#ffffff;
  --rust:#c0462a;
  --teal:#3e9a7a;
  --orange:#e27b45;
  --ink:#3a3a3a;
  --soft-pink:#f3c6c0;
  --soft-green:#cfe6c9;
  --soft-peach:#f7dcc4;
}
*{box-sizing:border-box;margin:0;padding:0}
html,body{width:1200px;height:900px;overflow:hidden}
body{background:var(--backdrop);font-family:"Open Sans",Arial,sans-serif;color:var(--ink);position:relative}
.page{position:absolute;top:160px;width:338px;height:476px;background:var(--paper);overflow:hidden}
.page--intro{left:70px}
.page--values{left:437px}
.page--tips{left:800px}
.abs{position:absolute}
.pattern-band{position:absolute;left:0;width:100%;height:18px;
  background:linear-gradient(90deg,var(--soft-pink),var(--soft-green),var(--soft-peach),var(--soft-green),var(--soft-pink))}
.pattern-band--bottom{bottom:0}
.pattern-band--top{top:0}
.headline{font-family:"Oswald",Arial,sans-serif;font-weight:600;line-height:1.05}
.small{font-size:4.6px;line-height:1.4}

/* intro page */
.intro-title{left:18px;top:28px;font-size:17px}
.intro-title .line1{color:var(--rust)}
.intro-title .line2{color:var(--teal)}
.brand{left:206px;top:36px;display:flex;align-items:center;gap:5px;font-weight:700;font-size:11.5px;color:var(--teal);white-space:nowrap}
.brand-dot{width:11px;height:11px;border-radius:50%;background:var(--orange);flex:none}
.mission{left:18px;top:94px;width:305px;border-top:1px solid var(--orange);border-bottom:1px solid var(--orange);padding:5px 0;
  color:var(--orange);font-weight:700;font-size:5.8px;line-height:1.45}
.intro-sub{left:18px;top:141px;width:305px;color:var(--teal);font-weight:700;font-size:8.5px;line-height:1.2}
.intro-body{left:18px;top:170px;width:305px;line-height:1.35}
.intro-body p{margin-bottom:3px}
.stop-bar{left:0;top:252px;width:16px;height:190px}
.stop-seg{position:absolute;left:0;width:16px;display:flex;align-items:center;justify-content:center}
.stop-seg span{transform:rotate(-90deg);white-space:nowrap;color:#fff;font-weight:700;font-size:5.5px}
.stop-step{left:30px;width:122px;z-index:2}
.stop-icon{width:12px;height:12px;border-radius:50%;background:var(--orange);display:flex;align-items:center;justify-content:center;margin-left:30px;margin-bottom:4px}
.observe-label{font-weight:700;color:var(--orange);font-size:4.6px;width:24px;flex:none}
.observe-row{display:flex;margin-bottom:2px}
.photo{left:150px;top:250px;width:188px;height:190px;background:linear-gradient(90deg,#ffffff 0%,#eef1f3 18%,#c9ccd0 60%,#8e96a0 100%)}
.intro-url{left:215px;top:432px;font-size:6px;font-weight:700;color:var(--ink);z-index:2}

/* values page */
.values-tag{left:10px;top:28px;background:var(--teal);color:#fff;font-weight:700;font-size:7.5px;padding:2px 18px 2px 6px}
.values-intro{left:14px;top:46px;width:312px;font-size:6.5px;font-weight:600;line-height:1.35}
.values-heading{left:14px;top:70px;color:var(--orange);font-weight:700;font-size:7.5px}
.values-lead{left:14px;top:82px;width:312px}
.value-box{position:absolute;border:1px solid var(--teal);border-radius:2px;padding:4px 4px;display:grid;grid-template-columns:1.2fr 1fr;column-gap:4px}
.value-box ul{list-style:none;min-width:0}
.value-box li{font-size:4.4px;font-weight:600;line-height:1;height:10.2px;display:flex;align-items:center;gap:3px;white-space:nowrap}
.value-box li::before{content:"";width:4px;height:4px;border-radius:50%;background:var(--orange);flex:none}
.box-a{left:14px;top:102px;width:152px;height:160px}
.box-b{left:172px;top:102px;width:154px;height:160px}
.box-c{left:14px;top:270px;width:152px;height:164px}
.step-title{color:var(--orange);font-weight:700;font-size:7.5px}
.step2{left:174px;top:272px;width:152px}
.step-lines{margin-top:4px}
.step-line{display:flex;align-items:center;gap:4px;height:10px;font-size:4.5px}
.step-line b{width:7px;height:7px;border:0.6px solid var(--ink);border-radius:50%;display:flex;align-items:center;justify-content:center;font-weight:400}
.step-line i{flex:1;border-bottom:0.6px solid var(--ink);height:5px}
.step3{left:174px;top:390px;width:152px}
.values-footer{left:0;top:453px;width:100%;height:20px;background:var(--rust);color:#fff;font-weight:700;font-size:7px;display:flex;align-items:center;padding-left:58px}

/* tips page */
.tips-title{left:0;top:24px;width:100%;text-align:center;font-size:14px;color:var(--rust)}
.tips-title span{color:var(--teal)}
.tips-promise{left:22px;top:46px;width:294px;height:34px;border:1.2px solid var(--teal);border-radius:6px;padding:4px 16px;text-align:center;font-size:5.3px;font-weight:700;line-height:1.4}
.tips-heading{left:0;top:88px;width:100%;text-align:center;color:var(--rust);font-weight:700;font-size:7.5px}
.tip-list{left:30px;top:104px;width:296px;list-style:none}
.tip{display:flex;align-items:flex-start;height:34px}
.tip-name{width:70px;color:var(--teal);font-weight:700;font-size:4.8px;line-height:1.3}
.tip-arrow{width:10px;height:10px;flex:none;margin:0 8px 0 2px}
.tip-text{flex:1;font-size:4.3px;line-height:1.4}
</style>
</head>
<body>

<section class="page page--intro">
  <h1 class="abs headline intro-title"><span class="line1">PEOPLE WORK BETTER</span><br><span class="line2">WHEN THEY FEEL GOOD</span></h1>
  <div class="abs brand"><span class="brand-dot"></span>Kestrel Orchard</div>
  <p class="abs mission">Kestrel Orchard develops programmes, initiatives and events to optimise wellbeing, personal development, workplace culture, job satisfaction, engagement, organisational commitment and to assist with change management.</p>
  <h2 class="abs intro-sub">We cannot control what happens to us in life but we can change the way we react</h2>
  <div class="abs intro-body small">
    <p>Stress happens because we are allowing fear, anger, disappointment and a host of other negative emotions to navigate our actions. By becoming aware of these emotions and allowing them to simply be, we can begin to gain control of how we react and respond to stressful situations.</p>
    <p>Our experience is always changing. Without awareness, mental patterns related to what we fear and what upsets us make life harder.</p>
    <p>S.T.O.P is a powerful, yet surprisingly basic strategy that helps you to be focused, alert, relaxed and at your emotional best when stressful moments present themselves in your life.</p>
    <p>Simply put, it's a four-step checklist to use anytime you want to ground yourself and get some insight into whatever is going on. The whole idea behind it is that by taking a very brief break—even less than one minute—you can determine the very best action to take in the moment.</p>
  </div>

  <div class="abs stop-bar">
    <div class="stop-seg" style="top:0;height:40px;background:var(--rust)"><span>S = STOP</span></div>
    <div class="stop-seg" style="top:40px;height:40px;background:var(--orange)"><span>T = TAKE</span></div>
    <div class="stop-seg" style="top:80px;height:60px;background:var(--teal)"><span>O = OBSERVE</span></div>
    <div class="stop-seg" style="top:140px;height:50px;background:var(--rust)"><span>P = PROCEED</span></div>
  </div>

  <div class="abs photo" role="img" aria-label="Photo of a smiling man in shirt and tie laughing at his office desk"></div>

  <div class="abs stop-step small" style="top:254px"><div class="stop-icon"><svg width="6" height="6" viewBox="0 0 10 10"><path d="M5 9 1 5a2.3 2.3 0 0 1 4-3 2.3 2.3 0 0 1 4 3z" fill="#fff"/></svg></div>Stop what you are doing. Press the pause button on your thoughts and actions.</div>
  <div class="abs stop-step small" style="top:292px"><div class="stop-icon"><svg width="6" height="6" viewBox="0 0 10 10"><path d="M5 9 1 5a2.3 2.3 0 0 1 4-3 2.3 2.3 0 0 1 4 3z" fill="#fff"/></svg></div>Take a few deep breaths to centre yourself and bring yourself fully into the present moment.</div>
  <div class="abs stop-step small" style="top:330px">
    <div class="stop-icon"><svg width="6" height="6" viewBox="0 0 10 10"><path d="M5 9 1 5a2.3 2.3 0 0 1 4-3 2.3 2.3 0 0 1 4 3z" fill="#fff"/></svg></div>
    <p style="margin-bottom:3px">Observe what is going on with your:</p>
    <div class="observe-row"><span class="observe-label">BODY</span><span>What physical sensations are you aware of (touch, sight, hearing, taste, smell)?</span></div>
    <div class="observe-row"><span class="observe-label">EMOTIONS</span><span>What are you feeling right now?</span></div>
    <div class="observe-row"><span class="observe-label">MIND</span><span>What assumptions are you making about you? What is the story you're telling yourself?</span></div>
  </div>
  <div class="abs stop-step small" style="top:412px">Proceed with whatever you were doing, making a conscious, intentional choice to incorporate what you just learned.</div>

  <div class="abs intro-url">www.kestrelorchard.co.nz</div>
  <div class="pattern-band pattern-band--bottom" role="img" aria-label="Decorative row of soft coloured leaves"></div>
</section>

<section class="page page--values">
  <div class="pattern-band pattern-band--top" role="img" aria-label="Decorative row of soft coloured leaves"></div>
  <h2 class="abs values-tag">VALUES</h2>
  <p class="abs values-intro">This exercise is designed to help you reach a better understanding of your most significant values.</p>
  <h3 class="abs values-heading">WHAT I VALUE MOST…</h3>
  <p class="abs values-lead small">From this list of values (both work and personal), select the ten that are most important to you - as guides for how to behave, or as components of a valued way of life. Feel free to add any values of your own to this list.</p>

  <div class="value-box box-a">
    <ul><li>Achievement</li><li>Advancement and promotion</li><li>Adventure</li><li>Affection (love and caring)</li><li>Arts</li><li>Challenging problems</li><li>Change and variety</li><li>Close relationships</li><li>Community</li><li>Competence</li><li>Competition</li><li>Cooperation</li><li>Country</li></ul>
    <ul><li>Creativity</li><li>Decisiveness</li><li>Democracy</li><li>Ecological awareness</li><li>Economic security</li><li>Effectiveness</li><li>Efficiency</li><li>Ethical practice</li><li>Excellence</li><li>Excitement</li><li>Fame</li><li>Fast living</li><li>Financial gain</li><li>Freedom</li></ul>
  </div>
  <div class="value-box box-b">
    <ul><li>ability</li><li>Physical challenge</li><li>Pleasure</li><li>Power and authority</li><li>Privacy</li><li>Public service</li><li>Purity</li><li>Quality of what I take part in</li><li>Quality relationships</li><li>Recognition (respect from</li><li>others, status)</li><li>Religion</li><li>Reputation</li><li>Responsibility and account</li></ul>
    <ul><li>Security</li><li>Self-Respect</li><li>Serenity</li><li>Sophistication</li><li>Stability</li><li>Status</li><li>Supervising others</li><li>Time freedom</li><li>Truth</li><li>Wealth</li><li>Wisdom</li><li>Work under pressure</li><li>Work with others</li><li>Working alone</li></ul>
  </div>
  <div class="value-box box-c">
    <ul><li>Friendships</li><li>Growth</li><li>Having a family</li><li>Helping other people</li><li>Helping society</li><li>Honesty</li><li>Independence</li><li>Influencing others</li><li>Inner harmony</li><li>Integrity</li><li>Intellectual status</li><li>Involvement</li><li>Job tranquility</li><li>Knowledge</li></ul>
    <ul><li>Leadership</li><li>Location</li><li>Loyalty</li><li>Market position</li><li>Meaningful work</li><li>Merit</li><li>Money</li><li>Nature</li><li>Being around people who</li><li>are open and honest</li><li>Order (tranquility,</li><li>stability, conformity)</li><li>Personal development</li></ul>
  </div>

  <div class="abs step2">
    <h3 class="step-title">STEP 2: ELIMINATION</h3>
    <p class="small" style="margin-top:3px">Now that you have identified ten, imagine that you are only permitted to have five values. Which five would you give up? Cross them off. Put them into order, the one that is most important to you first. Write it somewhere and refer to it when you can't make a decision, align yourself with what makes you feel good.</p>
    <div class="step-lines">
      <div class="step-line"><b>1</b><i></i></div>
      <div class="step-line"><b>2</b><i></i></div>
      <div class="step-line"><b>3</b><i></i></div>
      <div class="step-line"><b>4</b><i></i></div>
      <div class="step-line"><b>5</b><i></i></div>
    </div>
  </div>
  <div class="abs step3">
    <h3 class="step-title">STEP 3: SUPPORT YOURSELF</h3>
    <p class="small" style="margin-top:3px">Write it somewhere and refer to it when you can't make a decision, align yourself with what makes you feel good.</p>
  </div>

  <div class="abs values-footer">visit us-www.kestrelorchard.co.nz</div>
</section>

<section class="page page--tips">
  <h2 class="abs headline tips-title">10 TIPS TO IMPROVE <span>YOUR WELLBEING</span></h2>
  <p class="abs tips-promise">Yes, you will have to get off the couch and you might need to say no to burgers for lunch every day but we promise we won't turn you into lycra wearing vegans with prescriptions to Glimmerleaf!</p>
  <h3 class="abs tips-heading">SMALL CHANGES EVERY DAY CAN MAKE A HUGE DIFFERENCE.</h3>
  <ul class="abs tip-list">
    <li class="tip"><span class="tip-name">PUT ON YOUR WAKE UP GRIN</span><svg class="tip-arrow" viewBox="0 0 10 10"><circle cx="5" cy="5" r="5" fill="var(--orange)"/><path d="M3 5h4M5.3 3.2 7 5 5.3 6.8" stroke="#fff" stroke-width="1" fill="none"/></svg><span class="tip-text">Smile and think happy thoughts – that first 90 secs has a big impact on your day. If you start the day with bad thoughts, then it compounds – simply turn up the corners of your mouth you'll start to release endorphins and serotonin, your feel-good hormones.</span></li>
    <li class="tip"><span class="tip-name">DRINK LEMON AND WARM WATER FIRST THING</span><svg class="tip-arrow" viewBox="0 0 10 10"><circle cx="5" cy="5" r="5" fill="var(--orange)"/><path d="M3 5h4M5.3 3.2 7 5 5.3 6.8" stroke="#fff" stroke-width="1" fill="none"/></svg><span class="tip-text">It wakes up your digestion and gently hydrates you after a long night. A simple ritual that starts the day on the right foot – and it only takes a minute to make before the kettle boils for coffee.</span></li>
    <li class="tip"><span class="tip-name">EXERCISE</span><svg class="tip-arrow" viewBox="0 0 10 10"><circle cx="5" cy="5" r="5" fill="var(--orange)"/><path d="M3 5h4M5.3 3.2 7 5 5.3 6.8" stroke="#fff" stroke-width="1" fill="none"/></svg><span class="tip-text">It boosts the happy chemicals in your brain. So Be Active - get your heart rate going and stretch those muscles. At the very least take the stairs. To get your endorphins surging you'll need to really heavy breathe – so walk up those stairs faster, do your house work quicker – get that heart pumping.</span></li>
    <li class="tip"><span class="tip-name">EAT A BANANA</span><svg class="tip-arrow" viewBox="0 0 10 10"><circle cx="5" cy="5" r="5" fill="var(--orange)"/><path d="M3 5h4M5.3 3.2 7 5 5.3 6.8" stroke="#fff" stroke-width="1" fill="none"/></svg><span class="tip-text">Did you ever see a depressed chimp? Bananas help to lessen feelings of stress and anxiety due to high levels of tryptophan which converts to serotonin – one of those happy hormones. The high level of potassium helps you to be more alert and will give you energy.</span></li>
    <li class="tip"><span class="tip-name">PUT ON YOUR WOW!</span><svg class="tip-arrow" viewBox="0 0 10 10"><circle cx="5" cy="5" r="5" fill="var(--orange)"/><path d="M3 5h4M5.3 3.2 7 5 5.3 6.8" stroke="#fff" stroke-width="1" fill="none"/></svg><span class="tip-text">Go outside and Take Notice – The wind, the warmth, the cold, the trees, the blossom, the amazing sky, the moon. The world is full of things that make you go WOW, if you just slow down and Take Notice. Even better, go with a friend and Connect as well.</span></li>
    <li class="tip"><span class="tip-name">5 FRUIT AND VEG PER DAY</span><svg class="tip-arrow" viewBox="0 0 10 10"><circle cx="5" cy="5" r="5" fill="var(--orange)"/><path d="M3 5h4M5.3 3.2 7 5 5.3 6.8" stroke="#fff" stroke-width="1" fill="none"/></svg><span class="tip-text">Get the fibre into you… Without it you clog up, if you clog up you get grumpy and sluggish. If you get grumpy and sluggish – let's not go there! If you have trouble fitting the vegies in, put them into a smoothie.</span></li>
    <li class="tip"><span class="tip-name">PLAY MUSIC</span><svg class="tip-arrow" viewBox="0 0 10 10"><circle cx="5" cy="5" r="5" fill="var(--orange)"/><path d="M3 5h4M5.3 3.2 7 5 5.3 6.8" stroke="#fff" stroke-width="1" fill="none"/></svg><span class="tip-text">It cheers you up. Create a playlist for when you need a pick-me-up. Play it in the car to and from work, doing your housework or when you're going for that brisk walk, getting out of breath and send even more happy hormones to your brain. (No, not the sad break-up playlist!)</span></li>
    <li class="tip"><span class="tip-name">REMOVE A POISON</span><svg class="tip-arrow" viewBox="0 0 10 10"><circle cx="5" cy="5" r="5" fill="var(--orange)"/><path d="M3 5h4M5.3 3.2 7 5 5.3 6.8" stroke="#fff" stroke-width="1" fill="none"/></svg><span class="tip-text">Take away something that you know is bad for you – fast food, sugar, gluten – even for a couple of days a week – replace it with something healthy like water, fruit, veg, quinoa, exercise whatever works for you.</span></li>
    <li class="tip"><span class="tip-name">KILL EM WITH KINDNESS</span><svg class="tip-arrow" viewBox="0 0 10 10"><circle cx="5" cy="5" r="5" fill="var(--orange)"/><path d="M3 5h4M5.3 3.2 7 5 5.3 6.8" stroke="#fff" stroke-width="1" fill="none"/></svg><span class="tip-text">When you're feeling bad, do something nice for someone else and it will make their day and you'll feel even better. In fact, Give every day.</span></li>
    <li class="tip"><span class="tip-name">KEEP THE COGS TURNING</span><svg class="tip-arrow" viewBox="0 0 10 10"><circle cx="5" cy="5" r="5" fill="var(--orange)"/><path d="M3 5h4M5.3 3.2 7 5 5.3 6.8" stroke="#fff" stroke-width="1" fill="none"/></svg><span class="tip-text">Use it or lose it as they say – use your brain. Keep learning – something new every day.</span></li>
  </ul>
  <div class="pattern-band pattern-band--bottom" role="img" aria-label="Decorative row of soft coloured leaves"></div>
</section>

</body>
</html>
```